Dane Calloway Photography

Would like the Business card to have a cool logo. I’m targeting wedding/ engagement: portrait photography. My phone number on it. And my business email address.

Target Market(s)

Wedding/portrait/engagement photography.

```html
<!DOCTYPE html>
<html lang="en">
<head>
<meta charset="utf-8">
<title>Dane Calloway Photography — Business Card</title>
<link rel="stylesheet" href="https://fonts.googleapis.com/css2?family=Montserrat:wght@600&family=Tinos:wght@700&display=swap">
<style>
  :root {
    --backdrop: #2b2b2b;
    --ink: #0b0b0b;
    --paper: #ffffff;
    --paper-shade: #ececec;
    --front-shade: #161616;
  }
  * { margin: 0; padding: 0; box-sizing: border-box; }
  html, body {
    width: 1200px;
    height: 901px;
    overflow: hidden;
    background: var(--backdrop);
  }
  .card {
    position: absolute;
    left: 280px;
    width: 640px;
    height: 366px;
    overflow: hidden;
    box-shadow: 0 10px 28px rgba(0,0,0,0.45);
  }
  .card--front { top: 60px; background: var(--ink); }
  .card--back { top: 470px; background: var(--paper); }
  .card__arc {
    position: absolute;
    right: -260px;
    top: -120px;
    width: 620px;
    height: 620px;
    border-radius: 50%;
  }
  .card--front .card__arc { background: var(--front-shade); }
  .card--back .card__arc { background: var(--paper-shade); }
  .wordmark {
    position: absolute;
    left: 0;
    right: 0;
    text-align: center;
    font-family: "Montserrat", sans-serif;
    font-weight: 600;
    text-transform: uppercase;
    line-height: 1;
  }
  .wordmark__name { display: block; font-size: 40px; letter-spacing: 1px; }
  .wordmark__trade { display: block; font-size: 11px; letter-spacing: 7px; margin-top: 6px; }
  .card--front .wordmark { top: 150px; color: var(--paper); }
  .card--back .wordmark { top: 90px; color: var(--ink); }
  .contact {
    position: absolute;
    display: flex;
    align-items: flex-start;
    gap: 8px;
    font-family: "Tinos", serif;
    font-weight: 700;
    font-size: 17px;
    line-height: 1.1;
    color: var(--ink);
    white-space: nowrap;
  }
  .contact--address { left: 70px; top: 236px; }
  .contact--phone { left: 360px; top: 236px; }
  .contact--email { left: 360px; top: 272px; }
  .contact__icon { width: 26px; height: 26px; flex: none; }
  .contact__text { padding-top: 4px; }
</style>
</head>
<body>
  <section class="card card--front">
    <div class="card__arc"></div>
    <div class="wordmark">
      <span class="wordmark__name">Dane Calloway</span>
      <span class="wordmark__trade">Photography</span>
    </div>
  </section>

  <section class="card card--back">
    <div class="card__arc"></div>
    <div class="wordmark">
      <span class="wordmark__name">Dane Calloway</span>
      <span class="wordmark__trade">Photography</span>
    </div>

    <div class="contact contact--address">
      <svg class="contact__icon" viewBox="0 0 26 26" aria-hidden="true">
        <circle cx="13" cy="13" r="11.5" fill="none" stroke="#0b0b0b" stroke-width="1.6"/>
        <path d="M13 20c-3-3.6-4.5-6-4.5-8a4.5 4.5 0 0 1 9 0c0 2-1.5 4.4-4.5 8z" fill="none" stroke="#0b0b0b" stroke-width="1.6"/>
        <circle cx="13" cy="12" r="1.6" fill="#0b0b0b"/>
      </svg>
      <p class="contact__text">Address: 4817 Ridgeline Rd<br>Alder Falls, TX 75102</p>
    </div>

    <div class="contact contact--phone">
      <svg class="contact__icon" viewBox="0 0 26 26" aria-hidden="true">
        <circle cx="13" cy="13" r="11.5" fill="none" stroke="#0b0b0b" stroke-width="1.6"/>
        <path d="M9.2 7.5l2 2.6-1.2 1.6c.8 1.8 2.1 3.1 3.9 3.9l1.6-1.2 2.6 2-1.1 2c-4.6-.4-8.4-4.2-8.8-8.8z" fill="#0b0b0b"/>
      </svg>
      <p class="contact__text">(555) 201-4386</p>
    </div>

    <div class="contact contact--email">
      <svg class="contact__icon" viewBox="0 0 26 26" aria-hidden="true">
        <circle cx="13" cy="13" r="11.5" fill="none" stroke="#0b0b0b" stroke-width="1.6"/>
        <rect x="7.5" y="9" width="11" height="8" fill="none" stroke="#0b0b0b" stroke-width="1.4"/>
        <path d="M7.5 9l5.5 4.5L18.5 9" fill="none" stroke="#0b0b0b" stroke-width="1.4"/>
      </svg>
      <p class="contact__text">hello@danecallowayphoto.com</p>
    </div>
  </section>
</body>
</html>
```